Contact card for an aggressive entrepreneur

I am looking for a business/contact card as an individual. I operate under the company name The Varden Collective, LLC (but don't generally use that other than for billing). I have explored a few ideas and am now turning to artplaza to connect with people more creative than me. I am trying to capture a diverse set of passions, which I will summarize with the following keywords (which may or may not be ON the card and are in no particular order):

entrepreneur
shark diver
MBA
visionary
defenseman
marketing guru
hockey coach
teacher
reader
writer
cook
captain
scuba diver
beach bum
Type A
Brightwater
Vermont
New York
Montauk
founder
leader
focused
driven
teammate father

hope that makes some sense!
Updates

Please note the photo is for reference - unless there is a really creative way to use it I do not need a card with a head shot (I am not a model or an actor!)

Project Deadline Extended
Reason: There have been several requests to submit designs so we will close this project this Wednesday and select a design by this Friday. Thank you to all for your great ideas and submissions!

I am reviewing the designs and will select one by end of day tomorrow, Tuesday, EST
Thank you to all who participated!

Target Market(s)

everyone from business contacts to personal acquaintances

Industry/Entity Type

Business

Requirements
Must have
• Must be utterly original, extraordinary and memorable.
How it achieves that is up to you!
Essential contact information that needs to be included:

phone: (555) 374-1926
email: tomas@vardencollective.example
chat: tomas.varden
Nice to have
• A striking visual whether that is a photo or illustration
Some way of conveying the diversity of what I am and what I do
Feel free to use the printing or physical material of the card to make it stand out.
Should not have
• I am not into "logos" but that being said I do not want to limit creativity in any way so feel free to ignore any part of this brief if you disagree with me. No need to use the attached photo of me, but that's what I look like.

```html
<!DOCTYPE html>
<html lang="en">
<head>
<meta charset="utf-8">
<title>Tomas Varden – Contact Card</title>
<link rel="stylesheet" href="https://fonts.googleapis.com/css2?family=Saira+Condensed:wght@400;700&display=swap">
<style>
  :root {
    --page: #ffffff;
    --ink-dark: #141414;
    --ink-light: #ffffff;
    --ink-blue: #6cb6e8;
    --ink-yellow: #f7e900;
    --ink-orange: #e07a1e;
    --bg-top: #b79a6c;
    --bg-mid: #4a4642;
    --bg-low: #1f1f1f;
  }
  html, body {
    margin: 0;
    padding: 0;
    width: 1000px;
    height: 1200px;
    overflow: hidden;
    background: var(--page);
  }
  .card {
    position: absolute;
    left: 213px;
    top: 127px;
    width: 574px;
    height: 946px;
    overflow: hidden;
    font-family: "Saira Condensed", "Arial Narrow", sans-serif;
  }
  .portrait-area {
    position: absolute;
    inset: 0;
    background:
      radial-gradient(ellipse 38% 22% at 50% 30%, rgba(214,150,120,0.55), rgba(214,150,120,0) 70%),
      radial-gradient(ellipse 60% 60% at 50% 75%, #3a3836 0%, rgba(40,40,40,0) 75%),
      linear-gradient(180deg, var(--bg-top) 0%, #8c7a5c 22%, var(--bg-mid) 45%, #2c2b2a 75%, var(--bg-low) 100%);
  }
  .keywords {
    position: absolute;
    left: 21px;
    right: 21px;
    top: 16px;
  }
  .row {
    display: flex;
    justify-content: space-between;
    align-items: center;
    height: 67.5px;
    font-size: 40px;
    line-height: 1;
    white-space: nowrap;
  }
  .dark { color: var(--ink-dark); }
  .light { color: var(--ink-light); }
  .blue { color: var(--ink-blue); }
  .yellow { color: var(--ink-yellow); }
  .orange { color: var(--ink-orange); }
  .contact {
    font-weight: 700;
    height: 77px;
  }
  .contact.phone { font-size: 42px; letter-spacing: 7px; word-spacing: 8px; }
  .contact.email { font-size: 34.5px; word-spacing: 6px; }
  .contact.chat { font-size: 36px; letter-spacing: 14px; word-spacing: 10px; }
  .contact .bar { font-weight: 400; letter-spacing: 0; }
</style>
</head>
<body>
  <div class="card">
    <div class="portrait-area" role="img" aria-label="Photograph of the card owner in a dark suit and tie, leaning on a desk in a warmly lit office"></div>
    <div class="keywords">
      <div class="row"><span class="dark">Entrepreneur |</span><span class="light">shark diver |</span></div>
      <div class="row"><span class="light">MBA | visionary |</span><span class="yellow">defenseman |</span></div>
      <div class="row"><span class="blue">teacher |</span><span class="light">hockey coach |</span></div>
      <div class="row"><span class="light">reader |</span><span class="orange">writer |</span></div>
      <div class="row"><span class="yellow">cook |</span><span class="light">captain |</span></div>
      <div class="row"><span class="light">scuba diver |</span><span class="blue">scuba diver |</span></div>
      <div class="row"><span class="orange">beach bum |</span><span class="light">Type A |</span></div>
      <div class="row"><span class="light">Brightwater |</span><span class="yellow">Vermont |</span></div>
      <div class="row"><span class="blue">New York | Montauk |</span><span class="light">founder |</span></div>
      <div class="row">
        <span class="light">leader</span><span class="light">|</span>
        <span class="orange">focused</span><span class="orange">|</span>
        <span class="light">driven</span><span class="light">|</span>
        <span class="blue">driven</span><span class="blue">|</span>
      </div>
      <div class="row contact phone yellow"><span>phone: (555) 374-1926</span><span class="bar">|</span></div>
      <div class="row contact email light"><span>email: tomas@vardencollective.example</span><span class="bar">|</span></div>
      <div class="row contact chat blue"><span>chat: tomas.varden</span><span class="bar">|</span></div>
    </div>
  </div>
</body>
</html>
```